'Under Cold Glass' Thriller Movie Poster

Halcrow Pictures would like a poster design for their film 'Under Cold Glass'. It is a psychological thriller told through the eyes of Lulu Fenwick - a C list celebrity - who will do anything to keep her name in the press.

After a nightclub appearance, she gets kidnapped and wakes up in a basement, who holds her hostage for ransom money. Lulu tries to use her fame to help raise the money, but gets caught up in a web of lies and scandal.

The director envisages a close-up of Lulu in the basement, with only one side of her face lit. I have uploaded a few screen grabs and a wide shot which has a more expressive look if that works for your design better.

We want something eye-catchy and to fit the mood of the film.

Thank you for your time in advance.

Industry/Entity Type

Movie

Requirements
Must have
• Information at the bottom of the poster in the usually tall white font...
• A HALCROW PICTURES Production
• Starring DANIEL CORVELL HOLLY MARSDEN PATRICIA LOWDER DONELLE PRATT with MARCUS OSTRELL and PAULA DRENNIK
• Make Up & Hair by MAEVE TOLLAND Wardrobe NINA HOLLOWAY Editor GERALD TER MAASKANT Supervising Editor ANDERS KELLOCK Art Director WINSTON DOVER Music NIAMH CORBET Director of Photography FELIX HARTUNG
• Executive Producers OWEN PRICHARD TESSA PRICHARD SAM KELVERT and RAVI MEHTA Production Manager CORDELIA MARSDEN-VALE Associate Producer GAVIN ROLFE
• Screenplay by GRANT HOLLIS-DEKKER & CALLUM ARDEN Directed by CALLUM ARDEN
• In the main body of the poster - the title 'UNDER COLD GLASS'.

```html
<!DOCTYPE html>
<html lang="en">
<head>
<meta charset="utf-8">
<title>Under Cold Glass — Poster</title>
<link href="https://fonts.googleapis.com/css2?family=Cabin+Sketch:wght@400;700&family=Oswald:wght@400;500&display=swap" rel="stylesheet">
<style>
  :root {
    --backdrop: #e4e6e5;
    --paper: #ffffff;
    --ink: #111111;
    --eye-tone: #d9d9d9;
  }
  * { margin: 0; padding: 0; box-sizing: border-box; }
  html, body {
    width: 960px;
    height: 1200px;
    overflow: hidden;
    background: var(--backdrop);
  }
  .poster {
    position: absolute;
    left: 166px;
    top: 30px;
    width: 628px;
    height: 1140px;
    background: var(--paper);
    color: var(--ink);
    box-shadow: 0 2px 10px rgba(0,0,0,0.12);
  }
  .director-mark {
    position: absolute;
    left: 20px;
    top: 18px;
    display: flex;
    align-items: center;
    gap: 6px;
  }
  .director-mark .mark-square {
    width: 14px;
    height: 14px;
    background: var(--ink);
  }
  .director-mark .mark-name {
    font-family: "Oswald", sans-serif;
    font-weight: 500;
    font-size: 15px;
    line-height: 1;
    letter-spacing: 0.5px;
    color: var(--ink);
  }
  .eye-art {
    position: absolute;
    left: 150px;
    top: 245px;
    width: 380px;
    height: 255px;
  }
  .title {
    position: absolute;
    left: 0;
    right: 0;
    top: 520px;
    text-align: center;
    font-family: "Cabin Sketch", cursive;
    font-weight: 400;
    color: var(--ink);
  }
  .title .title-top {
    display: block;
    font-size: 84px;
    line-height: 1;
    letter-spacing: 4px;
  }
  .title .title-main {
    display: block;
    font-size: 190px;
    line-height: 0.95;
    letter-spacing: 10px;
  }
  .credits {
    position: absolute;
    left: 40px;
    right: 40px;
    top: 945px;
    text-align: center;
    font-family: "Oswald", sans-serif;
    color: var(--ink);
    text-transform: uppercase;
  }
  .credits .company {
    font-size: 10px;
    margin-bottom: 14px;
    letter-spacing: 0.3px;
  }
  .credits .block {
    font-size: 10.5px;
    line-height: 1.45;
    margin-bottom: 3px;
  }
  .credits .role {
    font-size: 6px;
    letter-spacing: 0.2px;
    margin: 0 2px 0 4px;
  }
  .credits .writers {
    margin-top: 16px;
  }
</style>
</head>
<body>
  <main class="poster">
    <div class="director-mark">
      <span class="mark-square"></span>
      <span class="mark-name">CALLUM ARDEN</span>
    </div>

    <svg class="eye-art" viewBox="0 0 380 255" role="img" aria-label="Hand-drawn black ink eye with lashes and a radiating iris">
      <rect width="380" height="255" fill="var(--eye-tone)"/>
    </svg>

    <h1 class="title">
      <span class="title-top">UNDER COLD</span>
      <span class="title-main">GLASS</span>
    </h1>

    <section class="credits">
      <p class="company"><span class="role">A</span> HALCROW PICTURES <span class="role">Production</span></p>
      <p class="block">
        <span class="role">Starring</span> DANIEL CORVELL HOLLY MARSDEN PATRICIA LOWDER DONELLE PRATT <span class="role">with</span> MARCUS OSTRELL <span class="role">and</span> PAULA DRENNIK
        <span class="role">Make Up &amp; Hair by</span> MAEVE TOLLAND
        <span class="role">Wardrobe</span> NINA HOLLOWAY <span class="role">Editor</span> GERALD TER MAASKANT
        <span class="role">Supervising Editor</span> ANDERS KELLOCK <span class="role">Art Director</span> WINSTON DOVER
        <span class="role">Music</span> NIAMH CORBET <span class="role">Director of Photography</span> FELIX HARTUNG
      </p>
      <p class="block">
        <span class="role">Executive Producers</span> OWEN PRICHARD TESSA PRICHARD SAM KELVERT <span class="role">and</span> RAVI MEHTA
        <span class="role">Production Manager</span> CORDELIA MARSDEN-VALE <span class="role">Associate Producer</span> GAVIN ROLFE
      </p>
      <p class="block writers">
        <span class="role">Screenplay by</span> GRANT HOLLIS-DEKKER &amp; CALLUM ARDEN <span class="role">Directed by</span> CALLUM ARDEN
      </p>
    </section>
  </main>
</body>
</html>
```